Startup that helps high growth companies expand to new office locations needs a polished website

Hello! We are a B2B startup helping fast growing companies expand to new office locations. We are in need of a polished, vibrant website that is modern and professional. Our mission is to accelerate tech-enabled economic opportunity beyond silicon valley.
- Our current site is: https://www.pellanworks.co
- We help companies in 3 steps: Discover, Expand, Align
- Discover = analysis on where a company should expand to
geographically
- Expand = manage the entire office build out process
- Align = ongoing support at the new office and help culturally aligning
new office to HQ
- Look through our deck which is attached in this brief and incorporate parts of our deck into the website, especially content and messaging! Slide 2 in particular is important, so I've taken a screenshot of it individually and attached it.
- Please also carefully read through our branding document which includes color palettes and examples of websites we like. However, we are open to any ideas you think are better in terms of color and font! https://slides.marnotech.io/deck/7Qz_K2pLwRt9XyVbN4cHsJ8dFmA3eUoGi5/view#page=n8k2m4q7_0_0
- We need a strong call to action for customers to contact us

We are also looking for a new logo! This logo should convey that we help companies expand beyond their current office locations.

Thanks! Looking forward to seeing your designs!

Target Market(s)

hypergrowth startups of 100-500 people

Logo Text

PellanWorks

Coding

Coded - Design and coding required

Number of Pages Required

2 page

Font styles to use
Sans Serif

Requirements
Must have
• - Clear call to action on landing page
• - A separate about us page. Please refer to the wireframe attached
• - Incorporate content from the current homepage at https://www.pellanworks.co/ (Discover, Expand, Align content, which are the 3 pieces of our offering)
• - Incorporate messaging in Slide 2 of attached company ppt. I've also taken a screenshot of it individually and attached it.
• - Testimonials sections on homepage
Nice to have
• - Incorporate other elements of the slide deck as you see fit

```html
<!DOCTYPE html>
<html lang="en">
<head>
<meta charset="utf-8">
<title>PellanWorks — Distributed teams are the future of work</title>
<link href="https://fonts.googleapis.com/css2?family=Inter:wght@300;400;500;700;800&family=Poppins:wght@300;400;500&display=swap" rel="stylesheet">
<style>
:root{
  --pink:#f5416a;
  --white:#ffffff;
  --ink:#333a40;
  --muted:#6b7278;
  --faint:#a9aeb3;
  --paper:#f5f5f5;
  --blue-deep:#0f4fa8;
  --blue-mid:#1c66c4;
  --teal-dark:#173f4f;
  --teal:#1f5566;
  --hero-a:#1d3a44;
  --hero-b:#4d7180;
  --hero-c:#2a2f33;
}
*{box-sizing:border-box;margin:0;padding:0}
html,body{width:1200px;height:2632px;overflow:hidden}
body{position:relative;font-family:"Inter",Helvetica,Arial,sans-serif;color:var(--ink);background:var(--white)}
.abs{position:absolute}

/* Hero */
.hero{position:absolute;left:0;top:0;width:1200px;height:638px;
  background:linear-gradient(160deg,var(--hero-b) 0%,var(--hero-a) 45%,var(--hero-c) 75%,#5a4630 100%)}
.hero-shade{position:absolute;inset:0;background:linear-gradient(90deg,rgba(20,40,50,.45),rgba(20,40,50,0) 60%)}
.brand{left:172px;top:30px;font-weight:700;font-size:24px;letter-spacing:1px;color:var(--white)}
.nav{left:803px;top:35px;display:flex;gap:16px;font-size:11.5px;font-weight:700;color:var(--white);letter-spacing:.3px}
.hero-lead{left:179px;top:208px;font-size:35px;font-weight:300;line-height:43px;color:var(--white)}
.hero-title{left:179px;top:302px;font-size:42px;font-weight:800;color:var(--white);letter-spacing:.5px}
.hero-sub{left:179px;top:349px;font-size:14px;color:var(--white)}
.btn{display:flex;align-items:center;justify-content:center;background:var(--pink);color:var(--white);
  font-weight:700;font-size:15px;letter-spacing:.6px;border-radius:22px}
.hero-btn{left:177px;top:393px;width:170px;height:40px}
.scroll-cue{left:589px;top:538px}

/* About */
.about{position:absolute;left:0;top:638px;width:1200px;height:564px;background:var(--paper)}
.about-photo{left:172px;top:90px;width:472px;height:381px;
  background:linear-gradient(180deg,#2a3440 0%,#4a4238 55%,#8a6a40 75%,#2c2e33 100%)}
.about-title{left:691px;top:94px;font-size:30px;font-weight:400;color:var(--ink)}
.about-text{left:691px;top:144px;width:325px;font-size:11.5px;line-height:15.6px;color:var(--muted)}
.about-text p+p{margin-top:15px}
.about-btn{left:686px;top:386px;width:165px;height:42px}

/* Services */
.services{position:absolute;left:0;top:1202px;width:1200px;height:424px;
  background:linear-gradient(180deg,var(--blue-mid) 0%,var(--blue-deep) 55%,#164a8a 100%)}
.service{position:absolute;top:96px;width:240px;text-align:center;color:var(--white)}
.service svg{display:block;margin:0 auto}
.service h3{margin-top:30px;font-size:16px;font-weight:700;letter-spacing:1px}
.service p{margin:16px auto 0;width:228px;font-size:11.5px;line-height:15px}

/* Feedback */
.feedback{position:absolute;left:0;top:1626px;width:1200px;height:649px;
  background:radial-gradient(ellipse at 50% 60%,#ffffff 0%,#f1f2f3 55%,#e3e5e7 100%)}
.fb-title{left:0;width:1200px;top:66px;text-align:center;font-family:"Poppins",sans-serif;font-size:26px;font-weight:500;color:#4a4f54}
.fb-sub{left:400px;width:400px;top:116px;text-align:center;font-family:"Poppins",sans-serif;font-size:11.5px;line-height:19px;color:var(--muted)}
.card-back{left:353px;top:486px;width:464px;height:22px;background:#fafafa;box-shadow:0 2px 8px rgba(0,0,0,.06)}
.card{left:333px;top:247px;width:500px;height:262px;background:var(--white);box-shadow:0 4px 18px rgba(0,0,0,.07)}
.avatar{left:534px;top:200px;width:98px;height:98px;border-radius:50%;border:5px solid var(--white);
  background:linear-gradient(160deg,#9aa3a8,#5d666c);box-shadow:0 3px 10px rgba(0,0,0,.15)}
.client-name{left:333px;width:500px;top:325px;text-align:center;font-family:"Poppins",sans-serif;font-size:16px;font-weight:500;color:var(--ink)}
.client-role{left:333px;width:500px;top:352px;text-align:center;font-family:"Poppins",sans-serif;font-size:11px;color:var(--faint)}
.client-quote{left:368px;width:430px;top:386px;text-align:center;font-family:"Poppins",sans-serif;font-size:11.5px;line-height:19px;color:var(--faint)}
.arrow{width:36px;height:36px;border-radius:50%;background:var(--white);box-shadow:0 2px 8px rgba(0,0,0,.08);display:flex;align-items:center;justify-content:center}
.arrow-prev{left:157px;top:359px}
.arrow-next{left:1006px;top:359px}
.dots{left:556px;top:571px;display:flex;gap:14px;align-items:center}
.dot{width:8px;height:8px;border-radius:50%;background:#d6d9dc}
.dot.active{width:10px;height:10px;background:#1c77d2}

/* Contact */
.contact{position:absolute;left:0;top:2275px;width:1200px;height:357px;
  background:linear-gradient(135deg,var(--teal) 0%,var(--teal-dark) 60%,#12333f 100%);color:var(--white)}
.cta-title{left:218px;top:50px;font-size:22px;font-weight:700;letter-spacing:.8px}
.cta-rule{left:218px;top:95px;width:48px;height:4px;background:var(--white)}
.contact-info{left:218px;top:129px;font-size:13px;line-height:24px;letter-spacing:.3px}
.contact-help{left:218px;top:200px;font-size:12px;line-height:19px}
.socials{left:218px;top:255px;display:flex;gap:10px}
.socials span{width:9px;height:9px;background:var(--white);border-radius:50%}
.copyright{left:218px;top:278px;font-size:11.5px}
.field-label{left:560px;font-size:11.5px}
.field-line{left:560px;width:420px;height:2px;background:var(--white)}
.send-btn{left:560px;top:2547px;width:420px;height:36px;border-radius:2px;position:absolute}
</style>
</head>
<body>

<header class="hero">
  <div class="hero-shade" role="img" aria-label="Upward view of glass office towers against a cloudy sky"></div>
  <div class="abs brand">PELLANWORKS</div>
  <nav class="abs nav"><span>HOME</span><span>OFFERING</span><span>CONTACT</span><span>BLOG</span></nav>
  <div class="abs hero-lead">Distributed teams are<br>the future of work.</div>
  <h1 class="abs hero-title">ARE YOU READY?</h1>
  <div class="abs hero-sub">We are your turnkey solution to grow beyond Silicon Valley</div>
  <div class="abs btn hero-btn">FINDOUT MORE</div>
  <svg class="abs scroll-cue" width="22" height="44" viewBox="0 0 22 44" aria-hidden="true">
    <rect x="4" y="1" width="14" height="24" rx="7" fill="none" stroke="#fff" stroke-width="1.6"/>
    <line x1="11" y1="7" x2="11" y2="12" stroke="#fff" stroke-width="1.6"/>
    <polyline points="5,33 11,39 17,33" fill="none" stroke="#fff" stroke-width="1.8"/>
  </svg>
</header>

<section class="about">
  <div class="abs about-photo" role="img" aria-label="Office building with lit glass storefront at dusk"></div>
  <h2 class="abs about-title">About PellanWorks</h2>
  <div class="abs about-text">
    <p>Lorem ipsum dolor sit amet, ornare at et sed aliquam bibendum, sed fermentum ac ac cursus consectetuer, lectus vel ante nisl, mauris taciti vivamus sed in, amet ligula et ipsum feugiat pellentesque a. Vivamus mauris nec turpis, elit at ut, vel morbi pede, aliquam quisque morbi. Dis vitae dapibus mollitia vestibulum, sem fusce vivamus nunc, pellentesque euismod et, dictumst egestas nonummy, per convallis nam fringilla luctus nisl.</p>
    <p>Non erat nunc, morbi aliquam a adipiscing tellus, libero congue a varius, eget nec. Ipsum vel nibh in sit, numquam dui commodo, nunc nec id, felis tempor risus lacus. Phasellus turpis erat libero donec, ut dignissim.</p>
  </div>
  <div class="abs btn about-btn">FINDOUT MORE</div>
</section>

<section class="services" role="img" aria-label="City skyline at dusk under a blue overlay">
  <div class="service" style="left:164px">
    <svg width="96" height="90" viewBox="0 0 96 90" fill="none" stroke="#fff" stroke-width="2.4">
      <circle cx="48" cy="48" r="18"/>
      <path d="M41 66v8h14v-8"/>
      <line x1="48" y1="6" x2="48" y2="18"/><line x1="6" y1="48" x2="18" y2="48"/><line x1="78" y1="48" x2="90" y2="48"/>
      <line x1="18" y1="18" x2="26" y2="26"/><line x1="78" y1="18" x2="70" y2="26"/>
      <line x1="18" y1="78" x2="26" y2="70"/><line x1="78" y1="78" x2="70" y2="70"/>
    </svg>
    <h3>DISCOVER</h3>
    <p>We help you identify and evaluate the best cities and towns to grow your team. From talent availability to cost of living, we bring all the key metrics you need to make a decision.</p>
  </div>
  <div class="service" style="left:480px">
    <svg width="90" height="90" viewBox="0 0 90 90" fill="none" stroke="#fff" stroke-width="2.4">
      <polyline points="14,26 14,14 26,14"/><line x1="14" y1="14" x2="34" y2="34"/>
      <polyline points="64,14 76,14 76,26"/><line x1="76" y1="14" x2="56" y2="34"/>
      <polyline points="14,64 14,76 26,76"/><line x1="14" y1="76" x2="34" y2="56"/>
      <polyline points="64,76 76,76 76,64"/><line x1="76" y1="76" x2="56" y2="56"/>
    </svg>
    <h3>EXPAND</h3>
    <p>We act as your expansion manager, running an operations blueprint from start-to-launch. We source talent, arrange real estate, coordinate travel, enable local resources, and manage any other requests.</p>
  </div>
  <div class="service" style="left:804px">
    <svg width="90" height="90" viewBox="0 0 90 90" fill="none" stroke="#fff" stroke-width="2.4">
      <rect x="13" y="13" width="29" height="29"/><rect x="48" y="13" width="29" height="29"/>
      <rect x="13" y="48" width="29" height="29"/><rect x="48" y="48" width="29" height="29"/>
    </svg>
    <h3>ALIGN</h3>
    <p>We serve as an ongoing concierge; supporting recruitment, employee onboarding, office operations, events, and any other needs to help the local team succeed and grow.</p>
  </div>
</section>

<section class="feedback" role="img" aria-label="Misty city skyline faded into white">
  <h2 class="abs fb-title">Client’s Feedback</h2>
  <p class="abs fb-sub">It is a long established fact that a reader will be distracted by the readable content of a page when looking at .</p>
  <div class="abs card-back"></div>
  <div class="abs card"></div>
  <div class="abs avatar" role="img" aria-label="Client portrait photo"></div>
  <div class="abs client-name">Jhon Doe</div>
  <div class="abs client-role">CEO at Northvane</div>
  <p class="abs client-quote">Lorem Ipsum is simply dummy text of the printing and typesetting has been the industry's standard dummy text ever since the when unknown printer took a galley of type and scrambled it to make a type specimen standard dummy. ext ever since the when unknown printer.</p>
  <div class="abs arrow arrow-prev"><svg width="14" height="4"><line x1="1" y1="2" x2="13" y2="2" stroke="#c9cdd0" stroke-width="1.5"/></svg></div>
  <div class="abs arrow arrow-next"><svg width="14" height="4"><line x1="1" y1="2" x2="13" y2="2" stroke="#2bb673" stroke-width="1.5"/></svg></div>
  <div class="abs dots"><span class="dot"></span><span class="dot active"></span><span class="dot"></span></div>
</section>

<footer class="contact">
  <h2 class="abs cta-title">LET'S GET STARTED.</h2>
  <div class="abs cta-rule"></div>
  <div class="abs contact-info">EMAIL:<br>HELLO@PELLANWORKS.CO<br>PHONE: (415) 555 0182</div>
  <div class="abs contact-help">Having trouble? Find the answer to your query here.<br>Don't hasitate to contact us!</div>
  <div class="abs socials"><span></span><span></span><span></span></div>
  <div class="abs copyright">©2019 by PellanWorks</div>
</footer>

<div class="abs field-label" style="top:2306px;color:#fff">Your Name</div>
<div class="abs field-line" style="top:2337px"></div>
<div class="abs field-label" style="top:2359px;color:#fff">Your Email Address</div>
<div class="abs field-line" style="top:2390px"></div>
<div class="abs field-label" style="top:2409px;color:#fff">Subject</div>
<div class="abs field-line" style="top:2441px"></div>
<div class="abs field-label" style="top:2467px;color:#fff">Your Message</div>
<svg class="abs" style="left:958px;top:2506px" width="20" height="18" aria-hidden="true">
  <g fill="#fff"><rect x="14" y="0" width="3" height="3"/><rect x="14" y="5" width="3" height="3"/><rect x="9" y="5" width="3" height="3"/><rect x="14" y="10" width="3" height="3"/><rect x="9" y="10" width="3" height="3"/><rect x="4" y="10" width="3" height="3"/></g>
</svg>
<div class="abs field-line" style="top:2525px"></div>
<div class="btn send-btn">SEND MESSAGE</div>

</body>
</html>
```